Building company business card

Design and print business cards for BRENTHOLM PTY LTD.
A residantial homes building company.
Mark Lantern already designed the company Logo.

```html
<!DOCTYPE html>
<html lang="en">
<head>
<meta charset="utf-8">
<title>BRENTHOLM PTY LTD – Business Card</title>
<link rel="stylesheet" href="https://fonts.googleapis.com/css2?family=Oswald:wght@500;600&family=Barlow:wght@400;500&display=swap">
<style>
  :root {
    --navy: #0f1d62;
    --navy-deep: #0b1852;
    --gold: #c69a45;
    --gold-dark: #9a6b1f;
    --gold-light: #e2c174;
    --paper: #f1f1f1;
    --backdrop: #2a2a2a;
    --web-text: #d3d7e8;
  }
  * { margin: 0; padding: 0; box-sizing: border-box; }
  html, body {
    width: 1200px;
    height: 1138px;
    overflow: hidden;
    background: var(--backdrop);
  }
  .canvas {
    position: relative;
    width: 1200px;
    height: 1138px;
  }
  .card {
    position: absolute;
    border-radius: 16px;
    overflow: hidden;
  }

  /* Front: navy side */
  .card-front {
    left: 274px;
    top: 186px;
    width: 622px;
    height: 376px;
    background: linear-gradient(135deg, var(--navy) 0%, var(--navy-deep) 100%);
  }
  .front-wordmark {
    position: absolute;
    left: 0;
    right: 0;
    top: 130px;
    text-align: center;
    font-family: "Oswald", sans-serif;
    font-weight: 600;
    font-size: 64px;
    line-height: 1;
    color: var(--gold);
    letter-spacing: 0.02em;
  }
  .front-web {
    position: absolute;
    left: 0;
    right: 0;
    top: 330px;
    text-align: center;
    font-family: "Barlow", sans-serif;
    font-weight: 500;
    font-size: 15px;
    letter-spacing: 0.85em;
    padding-left: 0.85em;
    color: var(--web-text);
    white-space: nowrap;
  }

  /* Back: white side */
  .card-back {
    left: 276px;
    top: 608px;
    width: 618px;
    height: 374px;
    background: var(--paper);
  }
  .back-wordmark {
    position: absolute;
    left: 52px;
    width: 212px;
    top: 150px;
    text-align: center;
    font-family: "Oswald", sans-serif;
    font-weight: 600;
    font-size: 44px;
    line-height: 1;
    color: var(--navy);
    white-space: nowrap;
  }
  .company-name {
    position: absolute;
    left: 320px;
    top: 76px;
    font-family: "Oswald", sans-serif;
    font-weight: 600;
    font-size: 30px;
    line-height: 1.2;
    color: var(--navy);
    white-space: nowrap;
  }
  .person-name {
    position: absolute;
    left: 320px;
    top: 146px;
    font-family: "Oswald", sans-serif;
    font-weight: 500;
    font-size: 20px;
    line-height: 1.2;
    color: var(--navy);
    white-space: nowrap;
  }
  .person-role {
    position: absolute;
    left: 320px;
    top: 172px;
    font-family: "Barlow", sans-serif;
    font-weight: 500;
    font-size: 15px;
    color: var(--navy);
  }
  .contact-list {
    position: absolute;
    left: 318px;
    top: 197px;
    list-style: none;
    font-family: "Barlow", sans-serif;
    font-weight: 500;
    font-size: 15px;
    color: var(--navy);
    white-space: nowrap;
  }
  .contact-item {
    display: flex;
    align-items: center;
    height: 22.5px;
  }
  .contact-icon {
    width: 14px;
    height: 14px;
    margin-right: 14px;
    flex: none;
  }
  .card-footer {
    position: absolute;
    left: 0;
    bottom: 0;
    width: 618px;
    height: 48px;
  }
  .registration {
    position: absolute;
    left: 318px;
    top: 341px;
    font-family: "Barlow", sans-serif;
    font-weight: 500;
    font-size: 15.5px;
    color: #ffffff;
    white-space: nowrap;
  }
</style>
</head>
<body>
<main class="canvas">

  <section class="card card-front" aria-label="Card front">
    <div class="front-wordmark">BRENTHOLM</div>
    <p class="front-web">www.brentholm-pl.com</p>
  </section>

  <section class="card card-back" aria-label="Card back">
    <div class="back-wordmark">BRENTHOLM</div>

    <h1 class="company-name">BRENTHOLM PTY LTD</h1>
    <h2 class="person-name">THEODOR (TED) VARNEY</h2>
    <p class="person-role">Director</p>

    <ul class="contact-list">
      <li class="contact-item">
        <svg class="contact-icon" viewBox="0 0 14 14" aria-hidden="true">
          <rect x="1" y="3" width="12" height="8.5" fill="var(--gold)"/>
          <path d="M1 3 L7 8 L13 3" fill="none" stroke="var(--paper)" stroke-width="1.2"/>
        </svg>
        tdv@brentholm-pl.com
      </li>
      <li class="contact-item">
        <svg class="contact-icon" viewBox="0 0 14 14" aria-hidden="true">
          <path d="M1 5 Q7 0.5 13 5 L11.5 6.5 L9.5 5.5 L9.5 4.3 Q7 3.4 4.5 4.3 L4.5 5.5 L2.5 6.5 Z" fill="var(--gold)"/>
          <rect x="3" y="7" width="8" height="5" rx="1" fill="var(--gold)"/>
        </svg>
        0412 608 314 &amp; 0437 592 146
      </li>
      <li class="contact-item">
        <svg class="contact-icon" viewBox="0 0 14 14" aria-hidden="true">
          <path d="M7 13.5 C3 9 2 7 2 5.5 A5 5 0 0 1 12 5.5 C12 7 11 9 7 13.5 Z" fill="var(--gold)"/>
          <circle cx="7" cy="5.5" r="1.8" fill="var(--paper)"/>
        </svg>
        PO Box 482, Greenvale East, VIC 3061
      </li>
    </ul>

    <svg class="card-footer" viewBox="0 0 618 48" aria-hidden="true">
      <defs>
        <linearGradient id="goldStrip" x1="0" x2="1" y1="0" y2="0">
          <stop offset="0" stop-color="var(--gold-dark)"/>
          <stop offset="1" stop-color="var(--gold-light)"/>
        </linearGradient>
      </defs>
      <rect x="0" y="33" width="280" height="15" fill="url(#goldStrip)"/>
      <path d="M290 0 L618 0 L618 48 L264 48 Z" fill="var(--navy)"/>
    </svg>
    <p class="registration">ABN-42 118 205 760 &nbsp;|&nbsp; CDB-U 51208</p>
  </section>

</main>
</body>
</html>
```